Help our pizza bases / flat breads fly off the shelves - You'll be seen in supermarkets New Zealand

Packaging design.
We have bought a product that is in desperate need of a complete re-brand. This includes a name, and a package design.
It is an rectangle shaped flat bread that can be used in many ways, and is presented 5 in a pack, in an unprinted flexible formed bottom, with a flat top film applied that is flat and ready to receive your design.
The product is mainly used as a pizza base bought by Mums to feed the family. It is also can be a pre dinner nibble like a pizza bread, and for quick and easy, you can cut one into 3 pieces, and toast in a pop-up toaster, before topping with whatever is in your fridge.
The current name is "Kelvo breads" which is just silly. The brand "Kelvo" needs to change to "Darby's Flat Breads" or whatever you might suggest. The product name might be "Gourmet Pizza Base" or "Gourmet Flat bread" as you like.
The look must get consumers to pick up the product and have a closer look. The nature of the graphics should emphasize the versatility and multi-usefulness, so the consumer can imagine what they will do with the product when they get it home. I feel that an informative pack will be better than a beautiful pack to get more sales. I have uploaded pictures showing the product currently in Supermarkets, and also a picture of the current product. Dimensions are 310 x 130mm.
You will need to leave room for: Barcode, Nutritional Panel, Cooking instructions, Storage instructions, Ingredients list and Company contact details - each one say 45 x 45mm or similar.
These details could go on the bottom of the low long side, as this is obscured while on shelf (see photo)
You will also highlight in your design, Preservative Free, 100% Natural, 5 Bases, Made with Olive oil, Hand made, and the variant (Roasted Garlic, or Original)
You will want to highlight the uses like: Pizza base, pizza bread, cut toast and top or similar.

```html
<!DOCTYPE html>
<html lang="en">
<head>
<meta charset="utf-8">
<title>Marlo Bakery – Gourmet Pizza Bases Original</title>
<link href="https://fonts.googleapis.com/css2?family=Bebas+Neue&family=Oswald:wght@500;700&family=Arvo&family=Raleway:wght@400;500&display=swap" rel="stylesheet">
<style>
  :root {
    --page: #ffffff;
    --wood-light: #fbe7a6;
    --wood-mid: #f4d27c;
    --wood-grain: #eab968;
    --brown: #3d1a0e;
    --teal: #00a0b4;
    --white: #ffffff;
    --icon-fill: rgba(255,255,255,0.85);
  }
  html, body { margin: 0; padding: 0; overflow: hidden; }
  body { width: 1200px; height: 1000px; background: var(--page); position: relative; font-family: 'Raleway', sans-serif; }

  .pack-lid { position: absolute; left: 33px; top: 250px; width: 1135px; height: 487px; }

  .wood-tab {
    position: absolute; left: 337px; top: -60px; width: 197px; height: 80px;
    background: linear-gradient(90deg, var(--wood-mid), var(--wood-light));
    border-radius: 60px 90px 0 0;
  }
  .wood-board {
    position: absolute; left: 0; top: 0; width: 1135px; height: 328px;
    background:
      linear-gradient(180deg, transparent 0 18%, rgba(234,185,104,0.35) 19%, transparent 21% 46%, rgba(234,185,104,0.3) 47%, transparent 49% 78%, rgba(234,185,104,0.35) 79%, transparent 81%),
      linear-gradient(90deg, var(--wood-mid), var(--wood-light) 30%, var(--wood-mid) 55%, var(--wood-light) 80%, var(--wood-mid));
  }

  .brand-name {
    position: absolute; left: 0; width: 1090px; top: 62px; text-align: center;
    font-family: 'Oswald', sans-serif; font-weight: 500; font-size: 54px; line-height: 1.2; color: var(--brown); margin: 0;
  }
  .brand-name .brand-dot {
    display: inline-block; width: 18px; height: 18px; border-radius: 50%; background: var(--brown);
    vertical-align: middle; margin-right: 14px;
  }
  .product-line {
    position: absolute; left: 0; width: 1130px; top: 125px; text-align: center;
    font-family: 'Oswald', sans-serif; font-weight: 500; font-size: 58px; line-height: 1; color: var(--brown); margin: 0;
  }
  .product-name {
    position: absolute; left: 343px; top: 186px; margin: 0;
    font-family: 'Bebas Neue', sans-serif; font-size: 120px; line-height: 1; color: var(--brown); letter-spacing: -1px;
  }
  .variant {
    position: absolute; left: 343px; top: 282px; margin: 0;
    font-family: 'Arvo', serif; font-size: 34px; line-height: 1; color: var(--teal);
  }

  .info-band { position: absolute; left: 0; top: 328px; width: 1135px; height: 159px; background: var(--teal); color: var(--white); }
  .cut-line { position: absolute; left: 0; top: 72px; width: 1135px; border-top: 2px dashed rgba(255,255,255,0.85); }

  .uses-title {
    position: absolute; left: 45px; top: 14px; margin: 0;
    font-family: 'Oswald', sans-serif; font-weight: 700; font-size: 21px; line-height: 23px; letter-spacing: 1.5px;
  }
  .use-icon { position: absolute; top: 6px; height: 58px; background: var(--icon-fill); opacity: 0.35; border-radius: 14px; }
  .use-label { position: absolute; top: 28px; font-size: 26px; line-height: 1; font-weight: 400; white-space: nowrap; }
  .use-bullet { position: absolute; top: 37px; width: 10px; height: 10px; border-radius: 50%; background: var(--white); }

  .claim-badge {
    position: absolute; left: 212px; top: 85px; width: 155px; height: 50px; box-sizing: border-box;
    border: 2px solid var(--white); border-radius: 7px; text-align: center;
    font-family: 'Oswald', sans-serif; font-weight: 700; color: var(--white); white-space: nowrap;
  }
  .claim-badge .small { display: block; font-size: 12px; line-height: 15px; letter-spacing: 0.5px; margin-top: 2px; }
  .claim-badge .large { display: block; font-size: 22px; line-height: 26px; }

  .made-note { position: absolute; left: 487px; top: 90px; width: 102px; margin: 0; font-size: 11px; line-height: 15px; }
  .olive-sprig { position: absolute; left: 598px; top: 90px; width: 50px; height: 48px; background: var(--icon-fill); opacity: 0.35; border-radius: 40% 10%; }

  .pack-count { position: absolute; left: 795px; top: 100px; margin: 0; font-size: 34px; line-height: 1; white-space: nowrap; }
  .pack-count span { font-size: 24px; }
</style>
</head>
<body>
  <section class="pack-lid">
    <div class="wood-tab" role="img" aria-label="Wood board tab where the bakery mascot sits"></div>
    <div class="wood-board" role="img" aria-label="Light pine wood board texture"></div>

    <p class="brand-name"><span class="brand-dot"></span>Marlo Bakery</p>
    <p class="product-line">-Gourmet-</p>
    <h1 class="product-name">PIZZA BASES</h1>
    <p class="variant">ORIGINAL</p>

    <div class="info-band">
      <p class="uses-title">USE IT AS<br>YOU LIKE!</p>

      <div class="use-icon" style="left:186px;width:52px" role="img" aria-label="Sketch of toppings"></div>
      <span class="use-label" style="left:264px">TOP it!</span>
      <span class="use-bullet" style="left:373px"></span>

      <div class="use-icon" style="left:404px;width:62px" role="img" aria-label="Sketch of a pizza on a peel"></div>
      <span class="use-label" style="left:482px">BAKE it!</span>
      <span class="use-bullet" style="left:600px"></span>

      <div class="use-icon" style="left:640px;width:72px" role="img" aria-label="Sketch of a folded flatbread"></div>
      <span class="use-label" style="left:735px">FOLD it!</span>
      <span class="use-bullet" style="left:859px"></span>

      <div class="use-icon" style="left:892px;width:77px" role="img" aria-label="Sketch of a rolled wrap"></div>
      <span class="use-label" style="left:994px">ROLL it!</span>

      <div class="cut-line"></div>

      <div class="claim-badge"><span class="small">PRESERVATIVE FREE</span><span class="large">100% NATURAL</span></div>
      <p class="made-note">Made handmade with 5 bases and natural olive oil.</p>
      <div class="olive-sprig" role="img" aria-label="Olive branch sketch"></div>
      <p class="pack-count">5 <span>PCS.</span></p>
    </div>
  </section>
</body>
</html>
```